Business Card Design Project

Doctor, Pain Management. Need a new business card design with appointment info on the back. New address is 18 Whitcombe Road, Suite 305, Brookfield, NJ 07790. Right now I believe the rest of the information is staying the same.

```html
<!DOCTYPE html>
<html lang="en">
<head>
<meta charset="utf-8">
<title>Harbor Pain Care – Business Card</title>
<link rel="stylesheet" href="https://fonts.googleapis.com/css2?family=Open+Sans:wght@400;700&family=Lato:wght@400&family=Arimo:wght@400&display=swap">
<style>
  :root {
    --page-bg: #8c8c8c;
    --card-white: #ffffff;
    --accent-orange: #e8601a;
    --ink-dark: #1d1d1d;
    --ink-grey: #7b7b7b;
    --rule-grey: #a9a9a9;
    --text-light: #ffffff;
    --photo-deep: #1f2530;
    --photo-mid: #5d6b7a;
    --photo-warm: #c2401a;
  }
  * { margin: 0; padding: 0; box-sizing: border-box; }
  html, body { width: 1200px; height: 1200px; overflow: hidden; }
  body { background: var(--page-bg); position: relative; font-family: "Open Sans", sans-serif; }

  .card { position: absolute; top: 310px; width: 366px; height: 594px; box-shadow: 2px 3px 6px rgba(0,0,0,.35); overflow: hidden; }
  .card-front { left: 234px; }
  .card-back { left: 628px; width: 368px; background: var(--card-white); }

  .front-photo {
    position: absolute; inset: 0;
    background:
      radial-gradient(ellipse 45% 55% at 10% 62%, rgba(240,90,30,.95), rgba(194,64,26,.55) 45%, transparent 75%),
      radial-gradient(ellipse 60% 50% at 55% 25%, #7d8a98, transparent 70%),
      linear-gradient(160deg, #3a1c18 0%, var(--photo-mid) 45%, var(--photo-deep) 100%);
  }

  .centered { position: absolute; left: 0; right: 0; text-align: center; color: var(--text-light); }
  .doctor-name { top: 294px; font-size: 20px; font-weight: 700; letter-spacing: 0; }
  .doctor-title { top: 320px; font-size: 15.5px; }

  .icon-row { position: absolute; top: 364px; left: 68px; width: 244px; height: 22px; }
  .icon-row .rule { position: absolute; top: 11px; height: 1px; background: rgba(255,255,255,.55); width: 60px; }
  .icon-row .rule.left { left: 0; }
  .icon-row .rule.right { right: 0; }
  .icon-row .icons { position: absolute; left: 64px; top: 0; display: flex; gap: 8px; }
  .icon { width: 21px; height: 21px; background: var(--accent-orange); display: flex; align-items: center; justify-content: center; }

  .contact-list { top: 396px; font-size: 15.5px; line-height: 21.5px; }
  .divider { position: absolute; top: 493px; left: 60px; width: 252px; height: 1px; background: rgba(255,255,255,.45); }
  .address { top: 504px; font-size: 15.5px; line-height: 21.5px; }

  .brand { position: absolute; top: 72px; left: 0; right: 0; text-align: center; }
  .brand-mark { display: block; width: 46px; height: 46px; border-radius: 50%; background: var(--accent-orange); margin: 0 auto 26px; }
  .brand-name { font-family: "Arimo", sans-serif; font-size: 28px; font-weight: 400; color: var(--ink-dark); }

  .appointment-title { position: absolute; top: 266px; left: 0; right: 0; text-align: center; font-family: "Lato", sans-serif; font-size: 26px; font-weight: 400; color: var(--ink-dark); }
  .field { position: absolute; left: 27px; width: 315px; height: 34px; border-bottom: 1.5px solid var(--rule-grey); font-family: "Lato", sans-serif; font-size: 22px; color: var(--ink-grey); }
  .field-name { top: 322px; }
  .field-date { top: 381px; }
  .field-time { top: 440px; }

  .reminder { position: absolute; top: 515px; left: 0; right: 0; text-align: center; font-family: "Lato", sans-serif; font-size: 15px; line-height: 23px; color: var(--accent-orange); }
</style>
</head>
<body>
  <section class="card card-front">
    <div class="front-photo" role="img" aria-label="Photo of a person's back with the spine and ribs highlighted in glowing orange"></div>
    <p class="centered doctor-name">DR. LIAN MORROW, M.D., PH.D.</p>
    <p class="centered doctor-title">Board Certified Anesthiologist</p>
    <div class="icon-row">
      <span class="rule left"></span>
      <div class="icons">
        <span class="icon"><svg width="13" height="13" viewBox="0 0 14 14"><path d="M3 1l3 3-2 2c1 2 2 3 4 4l2-2 3 3-2 2C6 12 2 8 1 3z" fill="#fff"/></svg></span>
        <span class="icon"><svg width="13" height="13" viewBox="0 0 14 14"><rect x="3" y="1" width="8" height="4" fill="#fff"/><rect x="1" y="5" width="12" height="5" fill="#fff"/><rect x="3" y="9" width="8" height="4" fill="#fff" stroke="#e8601a"/></svg></span>
        <span class="icon"><svg width="13" height="13" viewBox="0 0 14 14"><circle cx="7" cy="7" r="6" fill="#fff"/><path d="M4 4c2 1 2 3 4 3s1 3 2 4" stroke="#e8601a" fill="none"/></svg></span>
        <span class="icon"><svg width="13" height="13" viewBox="0 0 14 14"><rect x="1" y="3" width="12" height="8" fill="#fff"/><path d="M1 3l6 5 6-5" stroke="#e8601a" fill="none"/></svg></span>
      </div>
      <span class="rule right"></span>
    </div>
    <p class="centered contact-list">973.555.0142<br>973.555.0178<br>www.harborpaincare.com<br>frontdesk@harborpaincare.com</p>
    <span class="divider"></span>
    <p class="centered address">18 Whitcombe Road, Suite 305<br>Brookfield, NJ 07790</p>
  </section>

  <section class="card card-back">
    <div class="brand">
      <span class="brand-mark"></span>
      <span class="brand-name">Harbor Pain Care</span>
    </div>
    <h2 class="appointment-title">APPOINTMENT</h2>
    <div class="field field-name">NAME:</div>
    <div class="field field-date">DATE :</div>
    <div class="field field-time">TIME :</div>
    <p class="reminder">If unable to keep your appointment,<br>please contact us as soon as possible</p>
  </section>
</body>
</html>
```